NEW! Sports Supplement label
Vital Kinetic Laboratories
Project: NEW! Sports Supplement label
NEW! Sports Supplement label - Sports
Creative Brief
Looking for a new packaging design for a new line of products. This needs to be a clean label that delivers a scientific or medical feel in 3 colors with 4 lines for product descriptor sublines. <p><p> For Example: <p> • Muscle Recovery Acceleration <p> • Nitric Oxide Production <p> • Maximum Muscle Mass <p> • Improved Energy &amp; Focus <p><p> Use the following elements for presentation: <p><p> Name: VK260Q <p><p> 120 Capsules Dietary Supplement <p><p> The products are geared to Sports Supplements, Fat burners, preworkout supplements, sport drinks. <p><p> The fonts for the Product name and VKL logo must be destinctive elements and pop that adds value by providing consumers with instantly recognizable cues to help with the purchase decision making process. Preferrably reversed out white or black. <p> <p> Please see the following sites as example product labels for creative thought. They also provide actual full labels for your review: <p><p> http://www.plorvex.com/product/index.jsp?productId=48573920 http://www.plorvex.com/product/index.jsp?productId=48619375 http://www.plorvex.com/product/index.jsp?productId=48926054 <p><p> The label should be clean, in that it provides a clear, attractive space, with key information (4 line product descriptor mentioned above) on the front display panel necessary for a consumer to make a quick purchase decision. <p> The label should communicate a concise but informative message designed to make the consumer feel comfortable with the product by providing consumers with instantly recognizable cues (symbols of quality) to help with the purchase decision making process.
Sports
Sports nutrition products target a mass audience of consumers who have grown up knowing an active lifestyle has positive, long-term implications for health, fitness, weight management and longevity.
Please provide label design with color codes and in standard file formats with element layers. 2.75 x 7.00 4 x 9.375

```html
<!DOCTYPE html>
<html lang="en">
<head>
<meta charset="utf-8">
<title>VK260Q Label</title>
<link href="https://fonts.googleapis.com/css2?family=Arimo:wght@400;700&display=swap" rel="stylesheet">
<style>
  :root {
    --label-red: #e3231f;
    --label-black: #1a1414;
    --label-white: #ffffff;
    --side-light: #d9d9d9;
    --side-dark: #3a3a3a;
    --page-bg: #ffffff;
  }
  html, body {
    margin: 0;
    padding: 0;
    width: 1200px;
    height: 1035px;
    overflow: hidden;
    background: var(--page-bg);
    font-family: 'Arimo', Arial, sans-serif;
  }
  .canvas {
    position: relative;
    width: 1200px;
    height: 1035px;
  }
  .label {
    position: absolute;
    left: 117px;
    top: 42px;
    width: 993px;
    height: 913px;
  }
  .band-top {
    position: absolute;
    left: 0; top: 0;
    width: 846px; height: 111px;
    background: var(--label-red);
  }
  .band-bottom {
    position: absolute;
    left: 0; top: 845px;
    width: 846px; height: 68px;
    background: var(--label-red);
  }
  .panel {
    position: absolute;
    left: 0; top: 111px;
    width: 846px; height: 734px;
    background: var(--label-black);
  }
  .side-panel {
    position: absolute;
    left: 846px; top: 0;
    width: 147px; height: 913px;
    background: linear-gradient(90deg, var(--side-dark) 0%, var(--side-light) 100%);
  }
  .brand {
    position: absolute;
    left: 56px;
    top: 126px;
    color: var(--label-white);
    font-weight: 700;
    font-size: 100px;
    line-height: 1;
    letter-spacing: 2px;
  }
  .brand-name {
    position: absolute;
    left: 56px;
    top: 238px;
    color: var(--label-white);
    font-weight: 700;
    font-size: 24px;
    letter-spacing: 0.5px;
    text-transform: uppercase;
  }
  .product-name {
    position: absolute;
    left: 0;
    top: 300px;
    width: 846px;
    height: 300px;
  }
  .product-name text {
    font-family: 'Arimo', Arial, sans-serif;
    font-weight: 700;
    fill: var(--label-white);
  }
  .benefits {
    position: absolute;
    left: 58px;
    top: 667px;
    margin: 0;
    padding: 0;
    list-style: none;
    color: var(--label-white);
    font-size: 25px;
    line-height: 40px;
  }
  .benefits li {
    display: flex;
    align-items: center;
  }
  .benefits li::before {
    content: "";
    display: inline-block;
    width: 11px;
    height: 11px;
    background: var(--label-white);
    transform: rotate(45deg);
    margin-right: 22px;
  }
  .count {
    position: absolute;
    left: 670px;
    top: 730px;
    width: 120px;
    text-align: center;
    color: var(--label-white);
    font-weight: 700;
  }
  .count-number { font-size: 36px; line-height: 38px; display: block; }
  .count-unit { font-size: 23px; line-height: 30px; display: block; }
  .count-type { font-size: 17px; line-height: 22px; display: block; }
</style>
</head>
<body>
<div class="canvas">
  <div class="label">
    <div class="band-top"></div>
    <div class="panel"></div>
    <div class="band-bottom"></div>

    <div class="side-panel" role="img" aria-label="Decorative striped side panel of the label"></div>

    <div class="brand">VKL</div>
    <div class="brand-name">Vital Kinetic Laboratories</div>

    <svg class="product-name" viewBox="0 0 846 300">
      <text x="50" y="216" font-size="195" textLength="753" lengthAdjust="spacingAndGlyphs">VK260Q</text>
      <polygon points="50,256 803,246 803,278 50,264" fill="var(--label-red)"/>
    </svg>

    <ul class="benefits">
      <li>Muscle Recovery Acceleration</li>
      <li>Nitric Oxide Production</li>
      <li>Maximum Muscle Mass</li>
      <li>Improved Energy &amp; Focus</li>
    </ul>

    <div class="count">
      <span class="count-number">120</span>
      <span class="count-unit">Capsules</span>
      <span class="count-type">Dietary<br>Supplement</span>
    </div>
  </div>
</div>
</body>
</html>
```